business cards

we want our logos on the back
the information on it are on the design I've uploaded
come up with whatever you think is best, we want something professional, sophisticated and sleek.

```html
<!DOCTYPE html>
<html lang="en">
<head>
<meta charset="utf-8">
<title>Kestrel Health and Performance — Business Cards</title>
<link href="https://fonts.googleapis.com/css2?family=Lato:wght@400;700&family=Montserrat:wght@600&display=swap" rel="stylesheet">
<style>
  :root {
    --stage: #2b2b2b;
    --card-black: #1b1b1b;
    --card-white: #ffffff;
    --brand-green: #52b947;
    --ink-white: #ffffff;
    --ink-dark: #1c1c1c;
    --rule-grey: #8a8a8a;
  }
  * { margin: 0; padding: 0; box-sizing: border-box; }
  html, body { width: 1200px; height: 895px; overflow: hidden; }
  body {
    background: var(--stage);
    font-family: "Lato", Arial, sans-serif;
    position: relative;
  }
  .card {
    position: absolute;
    width: 560px;
    height: 320px;
    border-radius: 18px;
    overflow: hidden;
  }

  /* Back: logo side */
  .card--back {
    left: 60px; top: 90px;
    background: var(--card-black);
    display: flex; flex-direction: column; align-items: center; justify-content: center;
  }
  .brand {
    display: flex; align-items: center; gap: 14px;
  }
  .brand__mark {
    width: 22px; height: 22px; background: var(--brand-green);
  }
  .brand__name {
    font-family: "Lato", Arial, sans-serif;
    font-weight: 400;
    font-size: 54px;
    letter-spacing: 14px;
    color: var(--ink-white);
  }
  .brand__tagline {
    margin-top: 6px;
    font-size: 12px;
    letter-spacing: 9px;
    color: var(--ink-white);
    padding-bottom: 6px;
    border-bottom: 1px solid var(--rule-grey);
  }
  .brand__services {
    margin-top: 6px;
    font-size: 9.5px;
    letter-spacing: 1.5px;
    color: var(--brand-green);
  }

  /* Front: contact side */
  .card--front {
    left: 580px; top: 485px;
    background: var(--card-white);
  }
  .front__art { position: absolute; inset: 0; }
  .front__brand {
    position: absolute; left: 46px; top: 118px;
  }
  .front__brand .brand__name { color: var(--ink-dark); font-size: 36px; letter-spacing: 9px; }
  .front__brand .brand__mark { width: 16px; height: 16px; }
  .front__brand .brand__tagline {
    color: var(--ink-dark); font-size: 8px; letter-spacing: 5.5px; border: 0; margin-top: 4px;
  }
  .contact {
    position: absolute; right: 28px; top: 40px;
    text-align: right; color: var(--ink-white);
  }
  .contact__name {
    font-family: "Montserrat", Arial, sans-serif;
    font-weight: 600; font-size: 24px;
    color: var(--brand-green); letter-spacing: 0.5px;
  }
  .contact__roles { font-size: 14px; line-height: 1.3; margin-top: 4px; }
  .contact__list { list-style: none; margin-top: 22px; font-size: 14px; line-height: 1.55; }
  .contact__list li { display: flex; justify-content: flex-end; align-items: center; gap: 10px; }
  .icon { width: 13px; height: 13px; fill: var(--brand-green); flex: none; }
</style>
</head>
<body>

  <section class="card card--back" aria-label="Business card back">
    <div class="brand">
      <span class="brand__mark"></span>
      <span class="brand__name">KESTREL</span>
    </div>
    <div class="brand__tagline">HEALTH AND PERFORMANCE</div>
    <div class="brand__services">PHYSIO · S&amp;C · COACHING · PERSONAL TRAINING · REHAB · RECOVERY</div>
  </section>

  <section class="card card--front" aria-label="Business card front">
    <svg class="front__art" viewBox="0 0 560 320" width="560" height="320" aria-hidden="true">
      <path d="M430 0 Q300 120 272 320 L560 320 L560 0 Z" fill="var(--card-black)"/>
      <path d="M424 0 Q284 118 244 320 L272 320 Q300 120 430 0 Z" fill="var(--brand-green)"/>
    </svg>

    <div class="front__brand">
      <div class="brand">
        <span class="brand__mark"></span>
        <span class="brand__name">KESTREL</span>
      </div>
      <div class="brand__tagline">HEALTH AND PERFORMANCE</div>
    </div>

    <div class="contact">
      <div class="contact__name">MARCUS DELANY</div>
      <div class="contact__roles">
        Director-<br>Personal Trainer<br>Sport Nutritionist<br>BExSc
      </div>
      <ul class="contact__list">
        <li>03 9000 1482
          <svg class="icon" viewBox="0 0 24 24"><path d="M6.6 10.8a15 15 0 0 0 6.6 6.6l2.2-2.2a1 1 0 0 1 1-.25 11.4 11.4 0 0 0 3.6.57 1 1 0 0 1 1 1V20a1 1 0 0 1-1 1A17 17 0 0 1 3 4a1 1 0 0 1 1-1h3.5a1 1 0 0 1 1 1c0 1.25.2 2.45.57 3.57a1 1 0 0 1-.25 1z"/></svg>
        </li>
        <li>03 9000 1483
          <svg class="icon" viewBox="0 0 24 24"><path d="M6 2h12v6H6zM4 9h16a2 2 0 0 1 2 2v6h-4v5H6v-5H2v-6a2 2 0 0 1 2-2zm4 8v3h8v-3z"/></svg>
        </li>
        <li>hello@kestrelfitco.com.au
          <svg class="icon" viewBox="0 0 24 24"><path d="M2 5h20v14H2zm2 2v.5l8 5 8-5V7z"/></svg>
        </li>
        <li>17 Larkin St, Bayview West
          <svg class="icon" viewBox="0 0 24 24"><path d="M12 2a7 7 0 0 0-7 7c0 5 7 13 7 13s7-8 7-13a7 7 0 0 0-7-7zm0 9.5A2.5 2.5 0 1 1 12 6.5a2.5 2.5 0 0 1 0 5z"/></svg>
        </li>
      </ul>
    </div>
  </section>

</body>
</html>
```